Business Card Design

We are a General Practice - Family medicine
We also have Allied Health professionals working within our team

Industry/Entity Type

Business

Contact Information for Business Card

Front of the card to display:

BRAMBLEWICK MEDICAL
PHONE 6348 2917

5/41 Fennimore Parade
Launceston Tasmania 7284

Back of the card to display:

My Appointments
Date:
Time:
With:

Please remember to phone us on 6348 2917 to cancel your appointment if you can't keep it.
A fee applied to missed appointments

```html
<!DOCTYPE html>
<html lang="en">
<head>
<meta charset="utf-8">
<title>Bramblewick Medical – Business Card</title>
<link rel="stylesheet" href="https://fonts.googleapis.com/css2?family=Arimo:wght@400;700&display=swap">
<style>
  :root {
    --backdrop: #9dff00;
    --card: #ffffff;
    --sky: #4fd6f7;
    --leaf: #8fe03a;
    --ink-grey: #6b6b6b;
    --label-grey: #5a5a5a;
  }
  * { margin: 0; padding: 0; box-sizing: border-box; }
  html, body {
    width: 1200px;
    height: 742px;
    overflow: hidden;
    background: var(--backdrop);
    font-family: "Arimo", Arial, sans-serif;
  }
  .canvas { position: relative; width: 1200px; height: 742px; }
  .card {
    position: absolute;
    top: 219px;
    width: 519px;
    height: 303px;
    background: var(--card);
  }
  .card--front { left: 40px; }
  .card--back { left: 641px; }

  .centered { position: absolute; left: 0; width: 100%; text-align: center; white-space: nowrap; }

  .brand-mark { position: absolute; left: 226px; top: 66px; }
  .brand-name {
    top: 150px;
    font-size: 42px;
    font-weight: 400;
    color: var(--sky);
    letter-spacing: 0.5px;
  }
  .tagline {
    top: 222px;
    font-size: 13px;
    letter-spacing: 4px;
    color: var(--ink-grey);
  }
  .phone-line {
    top: 249px;
    font-size: 13px;
    font-weight: 700;
    color: var(--sky);
  }
  .phone-line .phone-number { color: var(--leaf); margin-left: 8px; }
  .address {
    top: 277px;
    font-size: 13px;
    font-weight: 700;
    color: var(--sky);
  }

  .appointments-title {
    top: 124px;
    font-size: 15px;
    font-weight: 700;
    color: var(--leaf);
  }
  .field-label {
    position: absolute;
    top: 161px;
    font-size: 15px;
    font-weight: 700;
    color: var(--label-grey);
  }
  .field-label--date { left: 36px; }
  .field-label--time { left: 237px; }
  .field-label--with { left: 397px; }
  .cancel-note {
    top: 282px;
    font-size: 11.5px;
    color: var(--leaf);
  }
</style>
</head>
<body>
<main class="canvas">
  <section class="card card--front" aria-label="Card front">
    <svg class="brand-mark" width="76" height="76" viewBox="0 0 76 76" aria-hidden="true">
      <circle cx="38" cy="38" r="36" fill="var(--leaf)"/>
    </svg>
    <p class="centered brand-name">Bramblewick Medical</p>
    <p class="centered tagline">HEALTHCARE CENTRE</p>
    <p class="centered phone-line">BramblewickMedical<span class="phone-number">6348 2917</span></p>
    <p class="centered address">5/41 Fennimore Parade Launceston Tasmania 7284</p>
  </section>

  <section class="card card--back" aria-label="Card back">
    <p class="centered appointments-title">My Appointments</p>
    <p class="field-label field-label--date">Date -</p>
    <p class="field-label field-label--time">Time -</p>
    <p class="field-label field-label--with">With -</p>
    <p class="centered cancel-note">Please remember to phone us on 6348 2917 to cancel your appointment if you can't keep it</p>
  </section>
</main>
</body>
</html>
```